Branding product image: TOMBEL (Golden Papaya) in Plastic Cup (Ready to Eat)

The product is sliced Fruit in Light syrup
Flavour: TOMBEL (Golden Papaya)
The temporary product name: TOMBEL
I want the product design to be something 'fun', 'natural', and 'colourful'
The design concept could be anything depends on your imagination, but it must be eye catchy and attractive.
Basically, I want you to be creative in designing the logo and the overall graphic design for the label.
The measurement is 20 cm (Length) x 6,5 cm (Height)
The target customers are young and health conscious audiences (10 years - 65 years old).
Create something different. Something extraordinary.
Brief summary about the fruit:
This fruit only grows in certain part of the world. It grows in mountain area that is in tropical climate. The fruit flesh has a yellowish-golden color. It has an extraordinary taste (unlike normal papaya) and it suits very well with any dishes from cold appetizer, white/ red meat, desserts, and cocktails.
I need a packaging design for Fruit Cup productThe product is sliced Fruit in Light syrup.There will be various flavours i.e. apple, lychee, peach, papaya, etc.However, you may design the product using one sample flavour (i.e. papaya) first, as the designs of other flavours could be adjusted afterwards.The temporary product name is: RICCANAI want the product design to be something 'fun', 'natural', and 'colourful'.The design concept could be anything depends on your imagination. Basically, I want you to be creative in designing the logo and the overall graphic design for the label. - Create something different. Something extraordinary -Additional:The measurement is 20cm (Length) x 5cm (Height).The target customers are young audiences (10 years - 35 years old).The product design must stand out in the supermarket shelf.It must be eye catchy and attractive.Thank you,Harold-PLEASE REFER TO DESIGN SAMPLE ATTACHED TO HAVE A BETTER UNDERSTANDING FOR THE PRODUCT CONCEPT- Added Wednesday, September 17, 2014
Project Deadline Extended Reason: Haven't found a good design. Added Friday, September 19, 2014
Project Deadline Extended Reason: Need more time for designers to finalize and perfect the design.Thank you,Harold Added Monday, September 29, 2014
Project Deadline Extended Reason: I haven't found a great design yet. Added Tuesday, February 24, 2015
Reason: Getting better designs now. Still Open to new ideas while refining the latest designs from some designers.
Please do your best in submitting other great designs!

```html
<!DOCTYPE html>
<html lang="en">
<head>
<meta charset="utf-8">
<title>LUPEDOS Fruit Cup Labels</title>
<link rel="stylesheet" href="https://fonts.googleapis.com/css2?family=Amatic+SC:wght@700&family=Arimo:wght@400;700&family=Parisienne&display=swap">
<style>
  :root {
    --brand-red: #e8463a;
    --leaf-green: #7cbf3c;
    --ink: #1d1d1d;
    --paper: #ffffff;
    --page: #ffffff;
    --band-yellow: #fbe3a0;
    --band-orange: #f6b04c;
    --band-coral: #ef7a55;
    --band-pink: #f2a7a0;
    --rule: #222222;
  }
  * { margin: 0; padding: 0; box-sizing: border-box; }
  html, body {
    width: 1200px; height: 810px; overflow: hidden;
    background: var(--page);
    font-family: "Arimo", Arial, sans-serif;
    color: var(--ink);
  }
  .label-sheet {
    width: 1200px; height: 810px;
    display: flex; flex-direction: column; justify-content: center; align-items: center;
    gap: 20px;
  }
  .label {
    position: relative;
    width: 860px; height: 178px;
    background: var(--paper);
    box-shadow: 0 1px 4px rgba(0,0,0,0.18);
    overflow: hidden;
  }
  .brand-row { position: absolute; top: 12px; left: 0; width: 100%; height: 24px; }
  .brand {
    position: absolute; top: 0;
    display: flex; align-items: center; gap: 4px;
    font-family: "Arimo", Arial, sans-serif; font-weight: 700;
    font-size: 18px; letter-spacing: 0.5px; color: var(--brand-red);
  }
  .brand-dot { width: 7px; height: 7px; border-radius: 50%; background: var(--leaf-green); margin-bottom: 10px; }
  .brand:nth-child(1) { left: 27px; }
  .brand:nth-child(2) { left: 209px; }
  .brand:nth-child(3) { left: 390px; }
  .brand:nth-child(4) { left: 571px; }
  .brand:nth-child(5) { left: 752px; }

  .fruit-art {
    position: absolute; left: 258px; top: 52px; width: 602px; height: 112px;
    border-radius: 50% 0 0 50% / 40% 0 0 40%;
  }
  .art-papaya { background: linear-gradient(175deg, var(--band-yellow) 0%, var(--band-orange) 45%, var(--band-coral) 60%, var(--band-yellow) 100%); }
  .art-apple  { background: linear-gradient(175deg, var(--band-yellow) 0%, var(--band-coral) 40%, var(--band-orange) 60%, var(--band-yellow) 100%); }
  .art-peach  { background: linear-gradient(175deg, var(--band-yellow) 0%, var(--band-orange) 50%, #f29545 62%, var(--band-yellow) 100%); }
  .art-lychee { background: linear-gradient(175deg, var(--band-yellow) 0%, var(--band-pink) 45%, #e0506a 58%, var(--band-yellow) 100%); }

  .nutrition {
    position: absolute; left: 4px; top: 54px; width: 252px; height: 78px;
    border: 1.5px solid var(--rule); background: var(--paper);
    display: flex; font-size: 6.2px; line-height: 1.25;
  }
  .nutrition-head { width: 72px; padding: 3px 4px; border-right: 1px solid var(--rule); }
  .nutrition-title { font-size: 11px; line-height: 1; margin-bottom: 3px; }
  .nutrition-head p { font-size: 6.4px; }
  .nutrition-head .note { font-size: 4.6px; margin-top: 3px; }
  .nutrition-table { flex: 1; border-collapse: collapse; }
  .nutrition-table td { padding: 0 3px; border-bottom: 0.6px solid var(--rule); white-space: nowrap; }
  .nutrition-table tr:first-child td { border-bottom: 1.2px solid var(--rule); }
  .nutrition-table tr:last-child td { border-bottom: none; }
  .nutrition-table .pct { text-align: right; }

  .maker {
    position: absolute; left: 4px; top: 138px; width: 290px;
    font-size: 9.5px; font-weight: 700; line-height: 1.3;
  }
  .maker .url { display: block; padding-left: 90px; }
  .net-weight { position: absolute; left: 300px; top: 154px; font-size: 10.5px; font-weight: 700; }
  .natural { position: absolute; left: 776px; top: 150px; font-family: "Amatic SC", cursive; font-size: 17px; }

  .flavour { position: absolute; text-align: center; width: 240px; left: 530px; top: 66px; }
  .flavour-kicker { font-family: "Amatic SC", cursive; font-size: 20px; line-height: 0.9; display: block; margin-left: 20px; }
  .flavour-name { font-family: "Amatic SC", cursive; font-size: 46px; line-height: 0.9; letter-spacing: 1px; display: block; }
  .flavour-syrup { font-family: "Parisienne", cursive; font-size: 24px; line-height: 1; display: block; margin-top: 4px; }
  .flavour.single { top: 78px; }
</style>
</head>
<body>
<main class="label-sheet">

  <section class="label">
    <div class="fruit-art art-papaya" role="img" aria-label="Flowing yellow and orange syrup bands with illustrated papaya halves"></div>
    <div class="brand-row">
      <span class="brand">LUPEDOS<span class="brand-dot"></span></span>
      <span class="brand">LUPEDOS<span class="brand-dot"></span></span>
      <span class="brand">LUPEDOS<span class="brand-dot"></span></span>
      <span class="brand">LUPEDOS<span class="brand-dot"></span></span>
      <span class="brand">LUPEDOS<span class="brand-dot"></span></span>
    </div>
    <div class="nutrition">
      <div class="nutrition-head">
        <h3 class="nutrition-title">Nutrition Facts</h3>
        <p>Serv. Size &nbsp;( &nbsp;g)</p><p>Calories 185</p><p>Calories from Fat 85</p>
        <p class="note">*Percent Daily Values (DV) are based on a 2,000 calorie diet</p>
      </div>
      <table class="nutrition-table">
        <tr><td>Amount/Serving %DV*</td><td></td><td>Amount/Serving %DV*</td><td></td></tr>
        <tr><td>Total Fat 9.5mg</td><td class="pct">15%</td><td>Total Carb. 19g</td><td class="pct">6%</td></tr>
        <tr><td>Sat. Fat 2mg</td><td class="pct">9%</td><td>Dietary Fiber 14g</td><td class="pct">55%</td></tr>
        <tr><td>Trans Fat 0mg</td><td class="pct">0%</td><td>Sugars 5g</td><td></td></tr>
        <tr><td>Cholesterol 0mg</td><td class="pct">0%</td><td>Protein 5.5g</td><td></td></tr>
        <tr><td>Sodium 72mg</td><td class="pct">3%</td><td></td><td></td></tr>
        <tr><td colspan="4">Vitamin A 22% • Vitamin C 1.5% • Calcium 3% • Iron 2%</td></tr>
      </table>
    </div>
    <p class="maker">Manufactured by Lupedos Company - Marlow Blv. CA 90210<span class="url">www.lupedos.com</span></p>
    <p class="net-weight">NET WT. 7OZ. (200g)</p>
    <p class="natural">100% NATURAL</p>
    <h2 class="flavour" style="top:56px"><span class="flavour-kicker">GOLDEN</span><span class="flavour-name">PAPAYA</span><span class="flavour-syrup">in light syrup</span></h2>
  </section>

  <section class="label">
    <div class="fruit-art art-apple" role="img" aria-label="Flowing coral and yellow syrup bands with illustrated apple halves"></div>
    <div class="brand-row">
      <span class="brand">LUPEDOS<span class="brand-dot"></span></span>
      <span class="brand">LUPEDOS<span class="brand-dot"></span></span>
      <span class="brand">LUPEDOS<span class="brand-dot"></span></span>
      <span class="brand">LUPEDOS<span class="brand-dot"></span></span>
      <span class="brand">LUPEDOS<span class="brand-dot"></span></span>
    </div>
    <div class="nutrition">
      <div class="nutrition-head">
        <h3 class="nutrition-title">Nutrition Facts</h3>
        <p>Serv. Size &nbsp;( &nbsp;g)</p><p>Calories 185</p><p>Calories from Fat 85</p>
        <p class="note">*Percent Daily Values (DV) are based on a 2,000 calorie diet</p>
      </div>
      <table class="nutrition-table">
        <tr><td>Amount/Serving %DV*</td><td></td><td>Amount/Serving %DV*</td><td></td></tr>
        <tr><td>Total Fat 9.5mg</td><td class="pct">15%</td><td>Total Carb. 19g</td><td class="pct">6%</td></tr>
        <tr><td>Sat. Fat 2mg</td><td class="pct">9%</td><td>Dietary Fiber 14g</td><td class="pct">55%</td></tr>
        <tr><td>Trans Fat 0mg</td><td class="pct">0%</td><td>Sugars 5g</td><td></td></tr>
        <tr><td>Cholesterol 0mg</td><td class="pct">0%</td><td>Protein 5.5g</td><td></td></tr>
        <tr><td>Sodium 72mg</td><td class="pct">3%</td><td></td><td></td></tr>
        <tr><td colspan="4">Vitamin A 22% • Vitamin C 1.5% • Calcium 3% • Iron 2%</td></tr>
      </table>
    </div>
    <p class="maker">Manufactured by Lupedos Company - Marlow Blv. CA 90210<span class="url">www.lupedos.com</span></p>
    <p class="net-weight">NET WT. 7OZ. (200g)</p>
    <p class="natural">100% NATURAL</p>
    <h2 class="flavour single"><span class="flavour-name">APPLE</span><span class="flavour-syrup">in light syrup</span></h2>
  </section>

  <section class="label">
    <div class="fruit-art art-peach" role="img" aria-label="Flowing orange and yellow syrup bands with illustrated peach halves"></div>
    <div class="brand-row">
      <span class="brand">LUPEDOS<span class="brand-dot"></span></span>
      <span class="brand">LUPEDOS<span class="brand-dot"></span></span>
      <span class="brand">LUPEDOS<span class="brand-dot"></span></span>
      <span class="brand">LUPEDOS<span class="brand-dot"></span></span>
      <span class="brand">LUPEDOS<span class="brand-dot"></span></span>
    </div>
    <div class="nutrition">
      <div class="nutrition-head">
        <h3 class="nutrition-title">Nutrition Facts</h3>
        <p>Serv. Size &nbsp;( &nbsp;g)</p><p>Calories 185</p><p>Calories from Fat 85</p>
        <p class="note">*Percent Daily Values (DV) are based on a 2,000 calorie diet</p>
      </div>
      <table class="nutrition-table">
        <tr><td>Amount/Serving %DV*</td><td></td><td>Amount/Serving %DV*</td><td></td></tr>
        <tr><td>Total Fat 9.5mg</td><td class="pct">15%</td><td>Total Carb. 19g</td><td class="pct">6%</td></tr>
        <tr><td>Sat. Fat 2mg</td><td class="pct">9%</td><td>Dietary Fiber 14g</td><td class="pct">55%</td></tr>
        <tr><td>Trans Fat 0mg</td><td class="pct">0%</td><td>Sugars 5g</td><td></td></tr>
        <tr><td>Cholesterol 0mg</td><td class="pct">0%</td><td>Protein 5.5g</td><td></td></tr>
        <tr><td>Sodium 72mg</td><td class="pct">3%</td><td></td><td></td></tr>
        <tr><td colspan="4">Vitamin A 22% • Vitamin C 1.5% • Calcium 3% • Iron 2%</td></tr>
      </table>
    </div>
    <p class="maker">Manufactured by Lupedos Company - Marlow Blv. CA 90210<span class="url">www.lupedos.com</span></p>
    <p class="net-weight">NET WT. 7OZ. (200g)</p>
    <p class="natural">100% NATURAL</p>
    <h2 class="flavour single"><span class="flavour-name">PEACH</span><span class="flavour-syrup">in light syrup</span></h2>
  </section>

  <section class="label">
    <div class="fruit-art art-lychee" role="img" aria-label="Flowing pink and yellow syrup bands with illustrated lychee fruits"></div>
    <div class="brand-row">
      <span class="brand">LUPEDOS<span class="brand-dot"></span></span>
      <span class="brand">LUPEDOS<span class="brand-dot"></span></span>
      <span class="brand">LUPEDOS<span class="brand-dot"></span></span>
      <span class="brand">LUPEDOS<span class="brand-dot"></span></span>
      <span class="brand">LUPEDOS<span class="brand-dot"></span></span>
    </div>
    <div class="nutrition">
      <div class="nutrition-head">
        <h3 class="nutrition-title">Nutrition Facts</h3>
        <p>Serv. Size &nbsp;( &nbsp;g)</p><p>Calories 185</p><p>Calories from Fat 85</p>
        <p class="note">*Percent Daily Values (DV) are based on a 2,000 calorie diet</p>
      </div>
      <table class="nutrition-table">
        <tr><td>Amount/Serving %DV*</td><td></td><td>Amount/Serving %DV*</td><td></td></tr>
        <tr><td>Total Fat 9.5mg</td><td class="pct">15%</td><td>Total Carb. 19g</td><td class="pct">6%</td></tr>
        <tr><td>Sat. Fat 2mg</td><td class="pct">9%</td><td>Dietary Fiber 14g</td><td class="pct">55%</td></tr>
        <tr><td>Trans Fat 0mg</td><td class="pct">0%</td><td>Sugars 5g</td><td></td></tr>
        <tr><td>Cholesterol 0mg</td><td class="pct">0%</td><td>Protein 5.5g</td><td></td></tr>
        <tr><td>Sodium 72mg</td><td class="pct">3%</td><td></td><td></td></tr>
        <tr><td colspan="4">Vitamin A 22% • Vitamin C 1.5% • Calcium 3% • Iron 2%</td></tr>
      </table>
    </div>
    <p class="maker">Manufactured by Lupedos Company - Marlow Blv. CA 90210<span class="url">www.lupedos.com</span></p>
    <p class="net-weight">NET WT. 7OZ. (200g)</p>
    <p class="natural">100% NATURAL</p>
    <h2 class="flavour single"><span class="flavour-name">LYCHEE</span><span class="flavour-syrup">in light syrup</span></h2>
  </section>

</main>
</body>
</html>
```